Website Redesign for Technology Focused Investment Bank

We need a website redesign for a technology and digital media focused investment banking firm. Think modern and forward thinking yet stable and smart. We provide mergers and acquisitions advisory services to our clients. Our target market are CEO's and CFO's (senior executives) that run and operate technology firms.

Larkstone Capital Partners - www.larkstonecapitalpartners.example

We are headquartered in Los Angeles, CA. Please do NOT use the Pemberly marker for anything.

We have the content and can update the photos as well.

We are looking for a "template" website we can update and edit with ease.

A competitive firm's website is: www.brackenhale.example Not sure I like it but I want it to look way better then this one.

Looking for a more modern version. Not too stuffy and conservative, please. Elegant, smart, updated and progressive/modern.
Updates

Color preferences:  Blue's including matching logo color. Grey's. You can add other colors if it flows well and looks clean and nice.

Menu:  Drop Down

Open to platform...please use one that most people can use, is reasonably priced if I need to buy it, and easy to update monthly and sometimes weekly.

Please use this website as a good example of what we are looking for (or similar version of it): www.quelmora.example

Thanks!
Derek P.

We are reviewing all submissions and will select one this week. Thank you everyone for your outstanding and creative designs you have sent us. We really appreciate it.

Thanks for everyone's hard work and creative input into our website design. We really appreciate it!

Target Market(s)

CEO's and CFO's, Entrepreneurs and Board Members of Technology Companies.

Industry/Entity Type

Investment

Font styles to use
Sans Serif

Colors
33a6d7
0492cd
0555a3
3176b5
85abd2
333333
5c5c5c
757575

Requirements
Must have
• Links to social media including plain circle icon, LinkedIn, Google+, Facebook, etc.

Must try to match logo color
Should not have
• No conservative, old looking colors or background. For example, no green marble look.

```html
<!DOCTYPE html>
<html lang="en">
<head>
<meta charset="utf-8">
<title>Larkstone Capital Partners</title>
<link href="https://fonts.googleapis.com/css2?family=Open+Sans:wght@300;400;600;700&display=swap" rel="stylesheet">
<style>
:root{
  --blue-deep:#0555a3;
  --blue:#0492cd;
  --sky:#33a6d7;
  --steel:#3176b5;
  --pale:#85abd2;
  --ink:#333333;
  --grey:#5c5c5c;
  --grey-light:#757575;
  --navy:#0c2a55;
  --navy-dark:#081f42;
  --rule:#e3e6ea;
  --panel:#f2f3f5;
}
*{box-sizing:border-box;margin:0;padding:0}
html,body{width:839px;height:1200px;overflow:hidden;background:#e9ebee}
body{font-family:"Open Sans",Arial,sans-serif;color:var(--ink);font-size:9px}
.page{width:839px;height:1200px;background:#fff;position:relative;overflow:hidden}
.wrap{width:760px;margin:0 auto;position:relative}
a{color:inherit;text-decoration:none}

/* header */
.site-header{height:112px;background:#fff;position:relative}
.brand{position:absolute;left:0;top:10px;width:190px;height:64px;background:#fff;box-shadow:0 1px 4px rgba(0,0,0,.15);display:flex;align-items:center;gap:8px;padding:0 12px}
.brand-mark{width:16px;height:16px;background:var(--blue-deep);flex:none}
.brand-name{font-size:12px;font-weight:600;color:var(--blue-deep);line-height:1.2}
.util-links{position:absolute;right:0;top:0;height:18px;display:flex;gap:12px;align-items:center;background:var(--blue-deep);color:#fff;padding:0 12px;font-size:8px}
.lang{display:flex;gap:4px}
.lang span{width:12px;height:8px;background:var(--pale);display:block}
.search{position:absolute;left:382px;top:34px;width:150px;height:20px;border:1px solid #cfd4da;border-radius:2px;font-size:8px;color:#999;padding:4px 8px;display:flex;justify-content:space-between;align-items:center}
.call{position:absolute;right:0;top:30px;display:flex;align-items:center;gap:6px}
.call-label{font-size:7px;color:var(--grey-light);letter-spacing:.5px}
.call-number{font-size:13px;font-weight:700;color:#d9392b}
.main-nav{position:absolute;left:0;right:0;top:84px;height:24px;display:flex;align-items:stretch;border-bottom:1px solid var(--rule)}
.main-nav a{font-size:8px;font-weight:600;color:var(--grey);display:flex;align-items:center;padding:0 11px;text-transform:uppercase}
.main-nav a.active{background:var(--blue-deep);color:#fff}

/* hero */
.hero{height:262px;position:relative;background:linear-gradient(180deg,#1d3f6e 0%,#5d88b4 38%,#4d6e8c 62%,#2c4660 100%)}
.hero-text{position:absolute;right:120px;top:104px;color:#fff;text-align:right;text-transform:uppercase;font-weight:300;line-height:1.05}
.hero-text .l1{font-size:24px;letter-spacing:1px}
.hero-text .l2{font-size:18px}
.hero-text .l3{font-size:15px}

/* sectors */
.sectors{display:grid;grid-template-columns:repeat(4,1fr);gap:10px;margin-top:14px}
.sector{background:var(--panel);height:128px;position:relative}
.sector h3{background:var(--blue-deep);color:#fff;font-size:10px;font-weight:600;padding:6px 10px}
.sector ul{list-style:none;padding:8px 10px;color:var(--grey)}
.sector li{font-size:8px;line-height:14px}
.sector li::before{content:"• ";color:var(--blue)}
.btn-more{display:inline-block;border:1px solid #c5cbd2;background:#fff;color:var(--grey);font-size:7px;padding:3px 8px;position:absolute;left:10px;bottom:8px}

/* about + news */
.about-news{display:flex;gap:30px;margin-top:24px;height:200px}
.about-photo{width:146px;height:118px;margin-top:34px;background:linear-gradient(160deg,#9fb0c2,#c9d3dc 50%,#7d8c9b);flex:none}
.about{flex:1}
.section-title{font-size:17px;font-weight:600;color:var(--blue-deep);margin-bottom:8px}
.about-body{display:flex;gap:14px}
.about p{font-size:8px;line-height:13px;color:var(--grey);margin-bottom:8px}
.about .more{color:var(--blue);font-size:8px}
.news{width:190px}
.news-item{border-bottom:1px solid var(--rule);padding:5px 0 7px}
.news-date{color:#d9392b;font-size:8px;font-weight:600}
.news-item p{font-size:8px;line-height:12px;color:var(--grey)}

/* clients */
.clients{margin-top:20px;height:76px;border-top:1px solid var(--rule);border-bottom:1px solid var(--rule);display:flex;align-items:center;justify-content:space-between;padding:0 10px}
.clients .arrow{width:20px;height:20px}
.client-name{font-size:22px;font-weight:700;color:#9a9fa6;width:140px;text-align:center}

/* tweets */
.tweets{background:var(--panel);height:140px;margin-top:12px;text-align:center;padding-top:20px}
.tweet-icon{width:26px;height:26px;border-radius:50%;background:var(--blue);margin:0 auto}
.handle{font-size:8px;color:var(--blue);margin:4px 0 6px}
.tweet{font-size:8px;line-height:12px;color:var(--grey);width:470px;margin:0 auto}
.dots{display:flex;gap:5px;justify-content:center;margin-top:10px}
.dots i{width:6px;height:6px;border-radius:50%;background:#c4c9cf;display:block}
.dots i.on{background:var(--blue-deep)}

/* footer */
.site-footer{position:absolute;left:0;right:0;top:1002px;bottom:0;background:var(--navy);color:#c9d5e6}
.footer-cols{display:flex;justify-content:space-between;padding-top:22px;height:134px;border-bottom:1px solid #27446e}
.footer-cols h4{color:#fff;font-size:11px;font-weight:600;margin-bottom:8px}
.footer-cols p{font-size:8px;line-height:12px}
.newsletter{width:230px}
.signup{display:flex;margin-top:8px}
.signup span{flex:1;background:#fff;color:#999;font-size:8px;padding:5px 8px}
.signup b{background:var(--blue);color:#fff;font-size:8px;padding:5px 10px;font-weight:600}
.social{display:flex;gap:5px}
.social span{width:20px;height:20px;background:var(--blue);display:block}
.social span:nth-child(2){background:#2b4f9a}
.social span:nth-child(3){background:#d0432f}
.social span:nth-child(4){background:var(--steel)}
.contact{width:220px}
.contact .email{color:var(--sky)}
.footer-nav{display:flex;justify-content:center;gap:16px;font-size:8px;color:#fff;padding-top:14px}
.copyright{text-align:center;font-size:7px;color:#8fa3c0;margin-top:12px;padding-bottom:8px}
</style>
</head>
<body>
<div class="page">

  <header class="site-header">
    <div class="wrap" style="height:112px">
      <a class="brand" href="#"><span class="brand-mark"></span><span class="brand-name">Larkstone<br>Capital Partners</span></a>
      <div class="util-links"><a href="#">Home</a><a href="#">About</a><a href="#">Contact</a><span class="lang"><span></span><span></span><span></span></span></div>
      <div class="search"><span>Search here</span>
        <svg width="9" height="9" viewBox="0 0 10 10"><circle cx="4" cy="4" r="3" fill="none" stroke="#888" stroke-width="1.3"/><line x1="6.3" y1="6.3" x2="9.3" y2="9.3" stroke="#888" stroke-width="1.3"/></svg>
      </div>
      <div class="call">
        <svg width="18" height="18" viewBox="0 0 20 20"><circle cx="10" cy="10" r="9" fill="var(--blue-deep)"/><path d="M7 5.5l2 2-1 1.3c.7 1.4 1.8 2.5 3.2 3.2l1.3-1 2 2-1.2 1.5c-3.6-.4-6.9-3.7-7.3-7.3z" fill="#fff"/></svg>
        <div><div class="call-label">CALL NOW</div><div class="call-number">+1 310 555 0142</div></div>
      </div>
      <nav class="main-nav">
        <a class="active" href="#">Services</a><a href="#">Transactions</a><a href="#">Research</a><a href="#">Private Equity</a><a href="#">Recommendations</a><a href="#">About the Founder</a><a href="#">Careers</a><a href="#">News &amp; Blog</a>
      </nav>
    </div>
  </header>

  <section class="hero" role="img" aria-label="Photo of glass office towers reflected in a city waterfront at dusk">
    <div class="hero-text"><div class="l1">We are technology</div><div class="l2">and digital media</div><div class="l3">industry M&amp;A experts</div></div>
  </section>

  <div class="wrap">
    <section class="sectors">
      <article class="sector"><h3>Software</h3><ul><li>Enterprise Software</li><li>Software as a Service (SaaS)</li><li>Healthcare IT</li><li>Financial Technology</li></ul><a class="btn-more" href="#">Read more...</a></article>
      <article class="sector"><h3>IT Services</h3><ul><li>Systems Integrators</li><li>Cloud Services</li><li>Value Added Resellers (VARs)</li></ul><a class="btn-more" href="#">Read more...</a></article>
      <article class="sector"><h3>Internet &amp; Digital Media</h3><ul><li>Online Marketing and Lead Gen</li><li>Online Media / Video and Search</li><li>Ad Networks, Ad Tech</li></ul><a class="btn-more" href="#">Read more...</a></article>
      <article class="sector"><h3>Mobile</h3><ul><li>Mobile Software</li><li>Mobile Services</li><li>Mobile Applications</li></ul><a class="btn-more" href="#">Read more...</a></article>
    </section>

    <section class="about-news">
      <div class="about-photo" role="img" aria-label="Photo of a modern office building exterior"></div>
      <div class="about">
        <h2 class="section-title">Why Us?</h2>
        <p>We are an independent investment bank and M&amp;A advisory firm focused exclusively on the global Technology and Digital Media sectors. Specifically, we execute mergers and acquisitions for the Software, IT Services, Internet and Digital Media industry sectors.</p>
        <p>Our professionals have completed over $20 billion in transactions to date and have experience in investment banking.</p>
        <a class="more" href="#">Read more...</a>
      </div>
      <aside class="news">
        <h2 class="section-title">Latest News</h2>
        <div class="news-item"><div class="news-date">July, 24 2014</div><p>Lorem ipsum is simply dummy text of the printing and typesetting industry.</p></div>
        <div class="news-item"><div class="news-date">July, 24 2014</div><p>Lorem ipsum is simply dummy text of the printing and typesetting industry.</p></div>
        <div class="news-item"><div class="news-date">July, 24 2014</div><p>Lorem ipsum is simply dummy text of the printing and typesetting industry.</p></div>
      </aside>
    </section>

    <section class="clients">
      <svg class="arrow" viewBox="0 0 20 20"><polyline points="13,3 6,10 13,17" fill="none" stroke="#aab0b7" stroke-width="2"/></svg>
      <span class="client-name">Norvane</span><span class="client-name">Quarto</span><span class="client-name">Delvix</span><span class="client-name">Brightmere</span>
      <svg class="arrow" viewBox="0 0 20 20"><polyline points="7,3 14,10 7,17" fill="none" stroke="#aab0b7" stroke-width="2"/></svg>
    </section>
  </div>

  <section class="tweets">
    <div class="tweet-icon"></div>
    <div class="handle">@LarkstoneTech</div>
    <p class="tweet">Lorem ipsum is simply dummy text of the printing and typesetting industry. Lorem ipsum has been the industry's standard dummy text ever since the 1500s.</p>
    <div class="dots"><i class="on"></i><i></i><i></i></div>
  </section>

  <footer class="site-footer">
    <div class="wrap">
      <div class="footer-cols">
        <div class="newsletter"><h4>Newsletter!</h4><p>Subscribe to our M&amp;A Quarterly Updates</p><div class="signup"><span>Enter your email</span><b>Subscribe</b></div></div>
        <div><h4>Follow Us</h4><div class="social"><span></span><span></span><span></span><span></span></div></div>
        <div class="contact"><h4>Contact Us</h4><p>Larkstone Capital Partners, LLC<br>1200 Harbor Crest Ave, Suite 300<br>Los Angeles, CA 90017<br>United States of America<br>Phone: +1 310 555 0142<br>Email: <span class="email">info@larkstonecapitalpartners.example</span></p></div>
      </div>
      <nav class="footer-nav"><a href="#">Home</a><a href="#">About</a><a href="#">Services</a><a href="#">Transactions</a><a href="#">Research</a><a href="#">Private Equity</a><a href="#">Recommendations</a><a href="#">About the Founder</a><a href="#">Careers</a><a href="#">News &amp; Blog</a></nav>
      <p class="copyright">Copyright © 2014 Larkstone Capital Partners. All Rights Reserved.</p>
    </div>
  </footer>

</div>
</body>
</html>
```